Website design for labour force (commercial truck driver) company

Looking for a Wordpress template (or design files in conjunction with a free Wordpress template).
Company tag line:
CargoLoop – On Demand, Professional Drivers
Real Drivers | Real Standards | Real Results
Logo design has already been completed and is attached

Company provides contract drivers to trucking companies. Target market is both the trucking companies looking for drivers and drivers looking for work.
Design to encompass header / footer and basic page design, navigation menu, home page, contact page. Customer will add content and additional pages over time.

```html
<!DOCTYPE html>
<html lang="en">
<head>
<meta charset="utf-8">
<title>CargoLoop – On Demand, Professional Drivers</title>
<link rel="stylesheet" href="https://fonts.googleapis.com/css2?family=Poppins:wght@400;500;600;700&display=swap">
<style>
:root{
  --green:#178a62;
  --green-dark:#0f6f4e;
  --dark:#262626;
  --ink:#1f1f1f;
  --muted:#6b6b6b;
  --light:#f0f0f0;
  --card:#f8f8f8;
  --white:#ffffff;
}
*{margin:0;padding:0;box-sizing:border-box}
html,body{width:1200px;height:5093px;overflow:hidden}
body{font-family:'Poppins',sans-serif;color:var(--ink);background:var(--white);position:relative}
.abs{position:absolute}
.pill{position:absolute;display:flex;align-items:center;justify-content:center;border-radius:30px;font-weight:600;font-size:14px;text-transform:uppercase;letter-spacing:.2px}
.pill-green{background:var(--green);color:var(--white)}
.pill-white{background:var(--white);color:var(--green)}
.pill-outline{border:2px solid var(--white);color:var(--white)}
.accent{color:var(--green)}
.arrow-dot{display:inline-block;width:13px;height:13px;border-radius:50%;background:currentColor;margin-left:7px;position:relative}
.arrow-dot::after{content:"";position:absolute;left:4px;top:3.5px;border-left:6px solid var(--white);border-top:3px solid transparent;border-bottom:3px solid transparent}
.pill-green .arrow-dot{background:var(--white)}
.pill-green .arrow-dot::after{border-left-color:var(--green)}
.pill-white .arrow-dot{background:var(--green)}
.pill-white .arrow-dot::after{border-left-color:var(--white)}

/* hero */
.hero-bg{position:absolute;left:0;top:0;width:1200px;height:710px;
  background:linear-gradient(90deg,rgba(20,30,40,.75) 0%,rgba(20,30,40,.25) 55%,rgba(0,0,0,0) 100%),
  radial-gradient(circle at 1030px 330px,#ffd27a 0,#e79a3e 90px,rgba(120,110,100,0) 360px),
  linear-gradient(180deg,#46596a 0%,#6c7a80 40%,#7d8a5c 62%,#3e5a2a 78%,#2f3a2c 100%);
  clip-path:polygon(0 0,1200px 0,1200px 563px,600px 690px,0 563px)}
.hero-stripe{position:absolute;left:0;top:0;width:1200px;height:712px;background:var(--green);
  clip-path:polygon(0 563px,600px 690px,1200px 563px,1200px 578px,600px 710px,0 578px)}
.logo{position:absolute;font-weight:700;font-size:26px;display:flex;align-items:center;gap:10px}
.logo .mark{width:22px;height:22px;border-radius:50%;background:var(--green)}
.nav{position:absolute;top:52px;left:470px;display:flex;gap:22px;font-size:14px;color:var(--white)}
.nav .on{color:var(--green)}
.hero-title{left:108px;top:200px;font-size:50px;line-height:58px;font-weight:700;color:var(--white)}
.hero-sub{left:110px;top:330px;font-size:16px;color:var(--white)}

/* about */
.about-photo{left:70px;top:728px;width:520px;height:428px;border-radius:60px 214px 214px 60px;
  background:linear-gradient(135deg,#cfd3d6 0%,#8e959b 55%,#3d4550 100%)}
.h2{font-size:38px;font-weight:700;color:var(--ink)}
.about-text{left:668px;width:420px;font-size:13px;line-height:24px;color:var(--muted)}

/* split */
.split-left{left:0;top:1206px;width:600px;height:606px;background:linear-gradient(160deg,#3a3a3a,#1f1f1f);
  clip-path:polygon(0 0,600px 0,600px 540px,0 606px)}
.split-right{left:600px;top:1206px;width:600px;height:606px;background:linear-gradient(160deg,#1d9a6e,#127a55);
  clip-path:polygon(0 0,600px 0,600px 606px,0 540px)}
.split-col{position:absolute;top:1340px;width:420px;text-align:center;color:var(--white)}
.split-col h3{font-size:34px;font-weight:600;margin-top:20px}
.split-col .rule{width:56px;height:3px;background:var(--white);margin:16px auto 28px}
.split-col p{font-size:13px;line-height:22px}
.split-icon{width:96px;height:96px;margin:0 auto}

/* why */
.why-item{position:absolute;width:250px}
.why-item h4{font-size:16px;font-weight:600}
.why-item p{font-size:13px;line-height:20px;color:var(--muted);margin-top:6px}
.why-item.right-al{text-align:right}
.why-icon{position:absolute;width:68px;height:68px;border-radius:50%;display:flex;align-items:center;justify-content:center;box-shadow:0 0 0 8px #f1f1f1}

/* opportunities */
.opps-bg{left:0;top:2293px;width:1200px;height:825px;background:var(--light);
  clip-path:polygon(0 60px,600px 0,1200px 60px,1200px 825px,0 825px)}
.filter-label{position:absolute;top:2482px;font-size:13px;color:var(--ink)}
.select{position:absolute;top:2512px;width:186px;height:38px;background:var(--white);border:1px solid #e1e1e1;border-radius:4px;font-size:11px;color:var(--muted);padding:11px 12px}
.select::after{content:"";position:absolute;right:12px;top:14px;width:6px;height:6px;border-right:1.5px solid #777;border-bottom:1.5px solid #777;transform:rotate(45deg)}
.job{position:absolute;width:312px;height:212px;background:var(--card);border-radius:6px;padding:20px 18px}
.job .icon{position:absolute;left:20px;top:20px;width:44px;height:44px;border-radius:50%;background:var(--green)}
.job h5{margin-left:58px;font-size:15px;font-weight:600;margin-top:4px}
.job .sub{margin-left:58px;font-size:11px;color:var(--muted);margin-top:2px}
.job .loc{font-size:13px;margin-top:22px;display:flex;align-items:center;gap:5px}
.job .tags{display:flex;gap:10px;margin-top:14px}
.tag{background:var(--white);border-radius:14px;font-size:11px;color:var(--muted);padding:5px 14px;display:flex;align-items:center;gap:6px}
.tag i{width:9px;height:9px;border-radius:2px;border:1.5px solid var(--green);display:inline-block}
.job .wide{margin-top:10px;display:inline-flex}

/* faq */
.faq{position:absolute;left:219px;width:760px;border-radius:26px;background:var(--white);box-shadow:0 2px 8px rgba(0,0,0,.12);font-size:13px;font-weight:600;padding:14px 26px}
.faq .chev{position:absolute;right:20px;top:14px;width:20px;height:20px;border-radius:50%;background:var(--green)}
.faq .chev::after{content:"";position:absolute;left:6px;top:6px;width:6px;height:6px;border-right:2px solid #fff;border-top:2px solid #fff;transform:rotate(45deg)}
.faq.open .chev::after{left:7px;top:4px;transform:rotate(135deg)}
.faq .ans{font-weight:400;color:var(--muted);margin-top:12px;font-size:12px}

/* insights */
.ins-bg{left:0;top:3792px;width:1200px;height:655px;background:var(--dark);
  clip-path:polygon(0 119px,600px 0,1200px 119px,1200px 655px,0 655px)}
.post-img{position:absolute;top:3968px;width:312px;height:164px}
.post-box{position:absolute;top:4132px;width:290px;height:198px;background:var(--white);padding:28px 28px}
.post-box .meta{font-size:12px;color:var(--ink)}
.post-box h6{font-size:16px;font-weight:600;line-height:23px;margin-top:12px}
.post-box p{font-size:12px;line-height:20px;color:var(--muted);margin-top:14px}

/* cta */
.cta{left:0;top:4444px;width:1200px;height:313px;background:linear-gradient(180deg,#1a946a,#137c57);color:var(--white);text-align:center}
/* footer */
.foot-h{position:absolute;top:4816px;font-size:15px;font-weight:600}
.foot-list{position:absolute;font-size:13px;line-height:25px;color:#444}
.vbar{position:absolute;top:4812px;width:3px;height:46px;background:var(--green)}
.social{position:absolute;top:5039px;width:30px;height:30px;border-radius:50%;border:1px solid #bbb}
</style>
</head>
<body>

<!-- HERO -->
<div class="hero-bg" role="img" aria-label="Semi truck driving on a highway through green fields at sunset"></div>
<div class="hero-stripe"></div>
<div class="logo" style="left:113px;top:40px;color:var(--white)"><span class="mark"></span>CargoLoop</div>
<nav class="nav"><span class="on">Home</span><span>For Companies</span><span>For Drivers</span><span>About Us</span><span>Contact</span></nav>
<div class="pill pill-green" style="left:955px;top:39px;width:132px;height:42px;text-transform:none;font-size:14px">Apply to Drive</div>
<h1 class="abs hero-title">Driving Your Fleet<br>Forward</h1>
<p class="abs hero-sub">Fast, reliable CDL drivers when and where you need them.</p>
<div class="pill pill-green" style="left:113px;top:403px;width:169px;height:46px">Find Drivers</div>
<div class="pill pill-white" style="left:293px;top:403px;width:155px;height:46px">Apply to Drive</div>

<!-- ABOUT -->
<div class="abs about-photo" role="img" aria-label="Portrait of the company founder framed by a speed-line graphic"></div>
<h2 class="abs h2" style="left:668px;top:790px">About <span class="accent">Us</span></h2>
<p class="abs about-text" style="top:860px">Lorem ipsum dolor sit amet, consectetur adipiscing elit, sed do eiusmod tempor incididunt ut labore et dolore magna minim exercitation ullamco laboris aliqua.</p>
<p class="abs about-text" style="top:948px">Sed ut perspiciatis unde omnis iste natus error sit voluptatem accusantium doloremque laudantium, totam rem aperiam, eaque ipsa quae ab illo inventore veritatis et quasi architecto beatae vitae dicta sunt explicabo.</p>
<div class="pill pill-green" style="left:668px;top:1080px;width:184px;height:50px">Learn More<span class="arrow-dot"></span></div>

<!-- SPLIT -->
<div class="abs split-left" role="img" aria-label="Row of parked trucks in dark tones"></div>
<div class="abs split-right" role="img" aria-label="Driver standing beside trucks in green tones"></div>
<div class="split-col" style="left:90px">
  <svg class="split-icon" viewBox="0 0 96 96" fill="none" stroke="#fff" stroke-width="3">
    <rect x="40" y="8" width="30" height="44"/><rect x="50" y="2" width="12" height="6"/>
    <path d="M46 16h6M58 16h6M46 26h6M58 26h6M46 36h6M58 36h6"/>
    <rect x="10" y="52" width="46" height="24"/><path d="M56 60h16l10 10v6H56z"/>
    <circle cx="22" cy="80" r="6"/><circle cx="70" cy="80" r="6"/>
  </svg>
  <h3>Trucking Companies</h3><div class="rule"></div>
  <p>Whether it's a last-minute route, peak season, or long-term coverage—CargoLoop connects you with experienced, DOT-compliant CDL drivers fast.</p>
  <div class="pill pill-outline" style="position:relative;width:156px;height:44px;margin:30px auto 0">Start Hiring</div>
</div>
<div class="split-col" style="left:695px">
  <svg class="split-icon" viewBox="0 0 96 96" fill="none" stroke="#fff" stroke-width="3">
    <circle cx="30" cy="24" r="12"/><path d="M16 20h28"/>
    <path d="M10 90V58c0-8 8-14 20-14s20 6 20 14v32"/><path d="M22 90V70M38 90V70"/>
    <rect x="52" y="14" width="26" height="20"/><path d="M78 20h8l6 8v6H78z"/>
    <circle cx="60" cy="38" r="4"/><circle cx="84" cy="38" r="4"/>
  </svg>
  <h3>Contract Drivers</h3><div class="rule"></div>
  <p>Drive when and where you want. Join our nationwide network of drivers and choose flexible jobs that fit your lifestyle.</p>
  <div class="pill pill-outline" style="position:relative;width:156px;height:44px;margin:30px auto 0">Apply to Drive</div>
</div>

<!-- WHY -->
<h2 class="abs h2" style="left:0;width:1200px;text-align:center;top:1836px">Why <span class="accent">CargoLoop</span></h2>
<svg class="abs" style="left:0;top:1900px" width="1200" height="330" fill="none" stroke="#d9d9d9" stroke-width="2">
  <path d="M445 71h50l40 35M755 71h-50l-40 35M445 267h50l40-35M755 267h-50l-40-35"/>
</svg>
<div class="abs" style="left:490px;top:1958px;width:218px;height:218px;border-radius:50%;background:#fff;box-shadow:0 4px 18px rgba(0,0,0,.14)"></div>
<div class="abs" style="left:508px;top:1976px;width:182px;height:182px;border-radius:50%;border:3px solid var(--green);display:flex;align-items:center;justify-content:center;font-weight:700;font-size:22px;color:var(--ink)">CargoLoop</div>

<div class="why-icon" style="left:375px;top:1937px;background:var(--dark)"><svg width="30" height="30" viewBox="0 0 30 30" fill="none" stroke="#fff" stroke-width="2"><rect x="4" y="6" width="16" height="18"/><path d="M20 12h5l3 5v7h-8"/><path d="M8 13l3 3 5-6"/></svg></div>
<div class="why-icon" style="left:749px;top:1937px;background:var(--green)"><svg width="30" height="30" viewBox="0 0 30 30" fill="none" stroke="#fff" stroke-width="2"><rect x="6" y="4" width="18" height="22" rx="2"/><path d="M10 11h10M10 16h10M10 21h6"/></svg></div>
<div class="why-icon" style="left:375px;top:2133px;background:var(--green)"><svg width="30" height="30" viewBox="0 0 30 30" fill="none" stroke="#fff" stroke-width="2"><rect x="4" y="6" width="22" height="16" rx="2"/><path d="M9 26h12M15 22v4M11 15l3 3 5-6"/></svg></div>
<div class="why-icon" style="left:749px;top:2133px;background:var(--dark)"><svg width="30" height="30" viewBox="0 0 30 30" fill="none" stroke="#fff" stroke-width="2"><circle cx="15" cy="15" r="11"/><path d="M4 15h22M15 4c4 4 4 18 0 22M15 4c-4 4-4 18 0 22"/></svg></div>

<div class="why-item right-al" style="left:92px;top:1930px"><h4>Pre-Vetted Drivers</h4><p>All drivers pass a strict screening process.</p></div>
<div class="why-item" style="left:852px;top:1930px"><h4>Flexible Contracts</h4><p>Temp, seasonal, or long-term support.</p></div>
<div class="why-item right-al" style="left:92px;top:2124px"><h4>Quick Deployment</h4><p>Get drivers on the road in 24–48 hours.</p></div>
<div class="why-item" style="left:852px;top:2124px"><h4>Nationwide Reach</h4><p>We cover all major U.S. freight corridors.</p></div>

<!-- OPPORTUNITIES -->
<div class="abs opps-bg"></div>
<h2 class="abs h2" style="left:0;width:1200px;text-align:center;top:2400px">Access the Best <span class="accent">Opportunities</span></h2>
<span class="filter-label" style="left:111px">Country</span>
<span class="filter-label" style="left:308px">Sector of activity</span>
<span class="filter-label" style="left:506px">Location</span>
<span class="filter-label" style="left:704px">Job Title</span>
<div class="select" style="left:111px">Select</div>
<div class="select" style="left:308px">Select</div>
<div class="select" style="left:506px">Select</div>
<div class="select" style="left:704px">What are you looking for</div>
<div class="pill pill-green" style="left:919px;top:2511px;width:168px;height:40px;font-size:13px">To Research</div>

<div class="job" style="left:111px;top:2596px"><span class="icon"></span><h5>Semi-Local Truck Driver</h5><p class="sub">Relocate to Colorado for this fleet job</p><p class="loc"><svg width="10" height="14" viewBox="0 0 10 14"><path d="M5 0a5 5 0 0 1 5 5c0 4-5 9-5 9S0 9 0 5a5 5 0 0 1 5-5z" fill="#178a62"/><circle cx="5" cy="5" r="2" fill="#fff"/></svg>Florida</p><div class="tags"><span class="tag"><i></i>Driving</span><span class="tag"><i></i>Contract</span></div><span class="tag wide"><i></i>Average Yearly Gross $74000</span></div>
<div class="job" style="left:445px;top:2596px"><span class="icon"></span><h5>Semi-Local Truck Driver</h5><p class="sub">Relocate to Colorado for this fleet job</p><p class="loc"><svg width="10" height="14" viewBox="0 0 10 14"><path d="M5 0a5 5 0 0 1 5 5c0 4-5 9-5 9S0 9 0 5a5 5 0 0 1 5-5z" fill="#178a62"/><circle cx="5" cy="5" r="2" fill="#fff"/></svg>Florida</p><div class="tags"><span class="tag"><i></i>Driving</span><span class="tag"><i></i>Contract</span></div><span class="tag wide"><i></i>Average Yearly Gross $74000</span></div>
<div class="job" style="left:777px;top:2596px"><span class="icon"></span><h5>Semi-Local Truck Driver</h5><p class="sub">Relocate to Colorado for this fleet job</p><p class="loc"><svg width="10" height="14" viewBox="0 0 10 14"><path d="M5 0a5 5 0 0 1 5 5c0 4-5 9-5 9S0 9 0 5a5 5 0 0 1 5-5z" fill="#178a62"/><circle cx="5" cy="5" r="2" fill="#fff"/></svg>Florida</p><div class="tags"><span class="tag"><i></i>Driving</span><span class="tag"><i></i>Contract</span></div><span class="tag wide"><i></i>Average Yearly Gross $74000</span></div>
<div class="job" style="left:111px;top:2827px"><span class="icon"></span><h5>Semi-Local Truck Driver</h5><p class="sub">Relocate to Colorado for this fleet job</p><p class="loc"><svg width="10" height="14" viewBox="0 0 10 14"><path d="M5 0a5 5 0 0 1 5 5c0 4-5 9-5 9S0 9 0 5a5 5 0 0 1 5-5z" fill="#178a62"/><circle cx="5" cy="5" r="2" fill="#fff"/></svg>Florida</p><div class="tags"><span class="tag"><i></i>Driving</span><span class="tag"><i></i>Contract</span></div><span class="tag wide"><i></i>Average Yearly Gross $74000</span></div>
<div class="job" style="left:445px;top:2827px"><span class="icon"></span><h5>Semi-Local Truck Driver</h5><p class="sub">Relocate to Colorado for this fleet job</p><p class="loc"><svg width="10" height="14" viewBox="0 0 10 14"><path d="M5 0a5 5 0 0 1 5 5c0 4-5 9-5 9S0 9 0 5a5 5 0 0 1 5-5z" fill="#178a62"/><circle cx="5" cy="5" r="2" fill="#fff"/></svg>Florida</p><div class="tags"><span class="tag"><i></i>Driving</span><span class="tag"><i></i>Contract</span></div><span class="tag wide"><i></i>Average Yearly Gross $74000</span></div>
<div class="job" style="left:777px;top:2827px"><span class="icon"></span><h5>Semi-Local Truck Driver</h5><p class="sub">Relocate to Colorado for this fleet job</p><p class="loc"><svg width="10" height="14" viewBox="0 0 10 14"><path d="M5 0a5 5 0 0 1 5 5c0 4-5 9-5 9S0 9 0 5a5 5 0 0 1 5-5z" fill="#178a62"/><circle cx="5" cy="5" r="2" fill="#fff"/></svg>Florida</p><div class="tags"><span class="tag"><i></i>Driving</span><span class="tag"><i></i>Contract</span></div><span class="tag wide"><i></i>Average Yearly Gross $74000</span></div>

<!-- FAQ -->
<h2 class="abs h2" style="left:0;width:1200px;text-align:center;top:3212px">Frequently Asked <span class="accent">Questions</span></h2>
<div class="faq" style="top:3315px">Lorem ipsum dolor sit amet, consectetur adipiscing elit, sed do eiusmod?<span class="chev"></span></div>
<div class="faq" style="top:3386px">Duis aute irure dolor in reprehenderit in velit esse cillum dolore?<span class="chev"></span></div>
<div class="faq" style="top:3457px">Lorem ipsum dolor sit amet, consectetur adipiscing elit, sed do eiusmod?<span class="chev"></span></div>
<div class="faq" style="top:3529px">Duis aute irure dolor in reprehenderit in velit esse cillum dolore?<span class="chev"></span></div>
<div class="faq open" style="top:3600px;border-radius:20px;padding-bottom:22px">Lorem ipsum dolor sit amet, consectetur adipiscing elit, sed do eiusmod?<span class="chev"></span><p class="ans">Sed ut perspiciatis unde omnis iste natus error sit voluptatem accusantium doloremque laudantium, totam</p></div>

<!-- INSIGHTS -->
<div class="abs ins-bg"></div>
<h2 class="abs h2" style="left:0;width:1200px;text-align:center;top:3880px;color:var(--white)">Industry <span class="accent">Insights</span></h2>
<div class="post-img" style="left:113px;background:linear-gradient(180deg,#b9c7cf 0%,#8a9a6a 55%,#5f6b45 100%)" role="img" aria-label="Yellow semi truck on a rural highway"></div>
<div class="post-img" style="left:445px;background:linear-gradient(180deg,#4f79a8 0%,#90a6b8 50%,#b9a27a 100%)" role="img" aria-label="White truck on a desert road at dusk"></div>
<div class="post-img" style="left:775px;width:312px;background:linear-gradient(180deg,#2d63b8 0%,#4c86d8 55%,#8fb3e2 100%)" role="img" aria-label="Driver standing in front of blue trucks"></div>
<div class="post-box" style="left:113px"><p class="meta">30 MAY 2024 &nbsp;/&nbsp; JOHN DOE</p><h6>Lorem ipsum dolor sit amet, consectetur elit,</h6><p>Sed ut perspiciatis unde omnis iste natus error sit voluptatem</p></div>
<div class="post-box" style="left:445px"><p class="meta"><span class="accent">30 MAY 2024 &nbsp;/&nbsp; JOHN DOE</span></p><h6>Lorem ipsum dolor sit amet, consectetur elit,</h6><p>Sed ut perspiciatis unde omnis iste natus error sit voluptatem</p></div>
<div class="abs" style="left:445px;top:4326px;width:96px;height:4px;background:var(--green)"></div>
<div class="post-box" style="left:775px"><p class="meta">30 MAY 2024 &nbsp;/&nbsp; JOHN DOE</p><h6>Lorem ipsum dolor sit amet, consectetur elit,</h6><p>Sed ut perspiciatis unde omnis iste natus error sit voluptatem</p></div>

<!-- CTA -->
<section class="abs cta" role="img" aria-label="Trucks on a highway under a green overlay">
  <h2 style="font-size:34px;font-weight:700;margin-top:56px">Ready to Move?</h2>
  <p style="font-size:15px;line-height:26px;width:800px;margin:14px auto 0">Lorem ipsum dolor sit amet, consectetur adipiscing elit, sed do eiusmod tempor incididunt ut labore et dolore magna aliqua.</p>
</section>
<div class="pill pill-white" style="left:371px;top:4643px;width:234px;height:46px">Start Hiring Today<span class="arrow-dot"></span></div>
<div class="pill pill-white" style="left:621px;top:4643px;width:207px;height:46px">Apply to Drive<span class="arrow-dot"></span></div>

<!-- FOOTER -->
<div class="logo" style="left:113px;top:4888px;color:var(--ink);font-size:30px"><span class="mark" style="width:26px;height:26px"></span>CargoLoop</div>
<span class="vbar" style="left:415px"></span>
<span class="vbar" style="left:763px"></span>
<span class="abs" style="left:415px;top:4870px;width:1px;height:135px;background:#e2e2e2"></span>
<span class="abs" style="left:763px;top:4870px;width:1px;height:135px;background:#e2e2e2"></span>
<h4 class="foot-h" style="left:494px">QUICK LINKS</h4>
<div class="foot-list" style="left:494px;top:4852px">Home<br>For Companies<br>For Drivers<br>About Us<br>Contact</div>
<div class="foot-list" style="left:631px;top:4852px">Support<br>Blog<br>Imprint<br>Careers</div>
<h4 class="foot-h" style="left:826px">CONTACT INFO</h4>
<div class="foot-list" style="left:826px;top:4852px;width:270px">
  <div style="display:flex;gap:12px"><svg width="14" height="18" viewBox="0 0 10 14" style="margin-top:4px;flex:none"><path d="M5 0a5 5 0 0 1 5 5c0 4-5 9-5 9S0 9 0 5a5 5 0 0 1 5-5z" fill="#178a62"/><circle cx="5" cy="5" r="2" fill="#fff"/></svg><span>480 Freight Way, Tulsa,<br>OK 74103</span></div>
  <div style="display:flex;gap:12px;margin-top:12px;align-items:center"><svg width="16" height="12" viewBox="0 0 16 12"><rect x="0.5" y="0.5" width="15" height="11" fill="#178a62"/><path d="M1 1l7 6 7-6" stroke="#fff" fill="none"/></svg>support@cargoloop.com</div>
  <div style="display:flex;gap:12px;margin-top:12px;align-items:center"><svg width="16" height="16" viewBox="0 0 16 16"><path d="M3 1l3 3-2 2c1 2 4 5 6 6l2-2 3 3-2 2C7 15 1 9 1 3z" fill="#178a62"/></svg><span style="text-decoration:underline">(800) 555-0148</span></div>
</div>
<div class="abs" style="left:113px;top:5016px;width:974px;height:1px;background:#e2e2e2"></div>
<p class="abs" style="left:113px;top:5044px;font-size:12px;color:#555">© 2025 CargoLoop. All Rights Reserved.</p>
<span class="social" style="left:546px"></span>
<span class="social" style="left:585px"></span>
<span class="social" style="left:624px"></span>
<p class="abs" style="left:866px;top:5044px;font-size:12px;color:#555;word-spacing:4px">Privacy &nbsp;| &nbsp;Terms &nbsp;| &nbsp;Disclaimer</p>

</body>
</html>
```